Steady Yield Spread Tactics for hurried readers

"Necessity is the mother of invention"

The idea of vetting investment strategies is not new in the financial world before investing real monies. Vetting strategies in options strategies always have been a difficult exercise. Such exercise requires access to programmers, right tools and good historical data. These factors make vetting process very costly and tedious. Becuase of this reason, this process is mostly limited to hedge funds, private banking, wealth management firms. Very few products existed in the market to support this process.

Since my graduation in engineering with major in Computer Science, I worked in large global banks as an IT consultant. Over there, I was designing, developing or managing large IT projects. This job profile demanded long hours, busy and tiring days. Very few hours or literally, not enough time available to analyze investment opportunities.

Moreover, investing in stocks without understanding valuation, business model and financials of the companies often result in losses. More so, if not enough understanding on when to exit from a position. Entering into a position is easy and it is in trader's control but exiting a position when profiting and cutting losses is an important step to make money consistently. This needed more disciplined approach and defined rules for position sizing, money management, profit taking and cutting losses.

Options have greeks that will affect its pricing. Understanding and leading options is another major step in the hurdle of investing in options. There are good mentors/experts teaching options. Gaining conceptual understanding is not that difficult. Practically seeing the market affecting the options trades is the most difficult step. Mentors/experts use primitive tools that give some peek into the practical process but it is very tedious since they often provide manual backtesting. "Options" provide options. There are a lot of questions that need to be answered.

Which options strategy is right?
How to select the expiration date for each options strategy?
How to select the strikes involved in options strategy?
There is an option to paper trade and gain knowledge in these areas. But it is a slow process. To speed things up, I founded Korvanto platform which speeds up vetting process. Moreover, all the tests done in the process of strategy design is remembered by the platform. If there a study that can deliver reward expectations for the acceptable risk amount, it can be locked to produce the trading opportunities on any interval. This makes it easy to use model for hurried readers.

The rest of the book is not to make you experts in all trading areas but it is targeted to help busy people with enough understanding to help you learn, trade carefully knowing that options trading has different risk characteristics. You can refer to them in detail on BXR website. All studies published in this book does not guarantee a future success but they have produced results in the past. These should be taken as educational reference.
Updates

This design is for Print book. Below is about the author. Book needs to have bar code printed and ISBN listed on the back as well. Ravindu Pemmasani, Founder, Korvanto Markets Ravindu is a computer science engineer with more than two decades of experience working for major financial institutions Norv, TL Holdings, and WQRB. During his time at Lumeridge Financial Services, he spearheaded a large global delivery team, led business growth in Latin America from the ground up, and was directly responsible for customer experience and software delivery. During this time, he discovered the passion for trading options. Leveraging this against his extensive experience in computer software architecture, Ravindu ventured out on his own to found and created www.korvantomarkets.example

Target Market(s)

Busy people with money and want to invest in stock market

Industry/Entity Type

Investment

Font styles to use
Sans Serif

Colors

Designer to choose colors to be used in the design.

Requirements
Must have
• 6 x 9 book. Title of book is "Steady Yield Spread Tactics" and the subtitle is "for hurried readers". The author is Ravindu Pemmasani.
• This is soft cover with 155 pages

```html
<!DOCTYPE html>
<html lang="en">
<head>
<meta charset="utf-8">
<title>Steady Yield Spread Tactics — Front Cover</title>
<link href="https://fonts.googleapis.com/css2?family=Montserrat:wght@600;700&family=Crimson+Pro:wght@500;600&display=swap" rel="stylesheet">
<style>
  :root {
    --backdrop: #e4e4e2;
    --cover-white: #ffffff;
    --ink: #111111;
    --rule-blue: #2a4aa8;
    --accent-red: #d8202a;
    --brand-navy: #2c3f8f;
    --brand-ink: #1c2233;
    --band-deep: #0b1f2a;
    --band-mid: #14465a;
    --band-glow: #1e6f8a;
  }
  * { box-sizing: border-box; margin: 0; padding: 0; }
  html, body {
    width: 1200px;
    height: 800px;
    overflow: hidden;
    background: var(--backdrop);
  }
  .stage {
    width: 1200px;
    height: 800px;
    display: flex;
    align-items: center;
    justify-content: center;
  }
  .front-cover {
    position: relative;
    width: 480px;
    height: 720px;
    background: var(--cover-white);
    box-shadow: 0 6px 24px rgba(0,0,0,0.18);
    display: flex;
    flex-direction: column;
    align-items: center;
  }
  .title {
    margin-top: 42px;
    font-family: "Montserrat", sans-serif;
    font-weight: 600;
    font-size: 58px;
    line-height: 62px;
    letter-spacing: -0.5px;
    color: var(--ink);
    text-align: center;
    text-transform: uppercase;
  }
  .title-rule {
    width: 330px;
    height: 4px;
    background: var(--rule-blue);
    margin-top: 10px;
  }
  .subtitle {
    margin-top: 8px;
    font-family: "Crimson Pro", serif;
    font-weight: 500;
    font-size: 27px;
    letter-spacing: 0.5px;
    color: var(--accent-red);
    text-transform: uppercase;
  }
  .hero-band {
    margin-top: 16px;
    width: 100%;
    height: 210px;
    background:
      radial-gradient(ellipse at 50% 70%, rgba(30,111,138,0.55), transparent 65%),
      linear-gradient(180deg, var(--band-deep) 0%, var(--band-mid) 55%, var(--band-deep) 100%);
  }
  .publisher {
    margin-top: 36px;
    display: flex;
    align-items: center;
    gap: 10px;
  }
  .publisher-mark {
    width: 34px;
    height: 34px;
    background: var(--brand-navy);
  }
  .publisher-name {
    font-family: "Montserrat", sans-serif;
    font-weight: 700;
    font-size: 28px;
    color: var(--brand-ink);
  }
  .author {
    margin-top: 30px;
    font-family: "Crimson Pro", serif;
    font-weight: 600;
    font-size: 25px;
    letter-spacing: 1px;
    color: var(--ink);
    text-transform: uppercase;
  }
</style>
</head>
<body>
  <main class="stage">
    <section class="front-cover">
      <h1 class="title">Steady<br>Yield<br>Spread<br>Tactics</h1>
      <div class="title-rule"></div>
      <p class="subtitle">for hurried readers</p>
      <div class="hero-band" role="img" aria-label="Photo of a trader seen from behind, facing a wall of glowing stock market charts with candlesticks and indicator lines"></div>
      <div class="publisher">
        <span class="publisher-mark"></span>
        <span class="publisher-name">Korvanto</span>
      </div>
      <p class="author">Ravindu Pemmasani</p>
    </section>
  </main>
</body>
</html>
```